Dermavale "polish what the seasons left you" The whole body approach to beauty, customized skincare a

I need a stronger logo design than what I have now. I currently have a small med spa in Chicago, IL. I will be expanding my brand to New York City and the Hamptons of NY. The services I provide in Chicago include; advanced medical grade skincare treatments, laser, plastic surgery and nutrition counsel. My concept is personalized skincare. Part of my philosophy is to dedicate a lot of time and make myself always available to my clients questions and concerns. To maintain integrity of the Dermavale Philosophy I do not advertise. Dermavale is an "exclusive skincare club" therefore you must be referred by an existing client or staff member in order to get an appointment. My Chicago clientele consists of young professionals competing with their peers to look their absolute best. The New York and Hamptons business has a completely different structure. It is a Mobile med spa service providing treatments at people's homes. The services provided are advanced skincare, wellness, massage, spray tan, hair and makeup. My vision for the new logo design is to exude an image that is both cutting edge, relevant, sophisticated, sexy and modern (sleek) yet practical and strong. It must be eye catching yet simplistic, aesthetically pleasing to look at and above all must promote EXCLUSIVITY! bellow I have attached my current logo design which is printed using silver and gold foil. The other is the logo on my prescription skincare products. I need to merge the two for the brand to be cohesive. I would like to print my business cards on a mirror like material where you can see your reflection. Front of card: the brand Dermavale across the front and across the bottom will be Chicago. New York. Hamptons Back of card: in a font style like writing "Dermavale is the whole body approach to beauty. customized medical grade skincare. massage. wellness counsel. By appointment only
www.dermavalewellness-example.com p: (555) 318-2406
I am open to all suggestions to make my brand as strong as possible. Please be creative and relevant. Thank you!

```html
<!DOCTYPE html>
<html lang="en">
<head>
<meta charset="utf-8">
<title>Dermavale — Business Card</title>
<link rel="stylesheet" href="https://fonts.googleapis.com/css2?family=Inter:wght@300&family=Parisienne&display=swap">
<style>
  :root {
    --backdrop: #ebe8e4;
    --card: #ffffff;
    --ink-soft: #a3a3a3;
    --ink-logo: #8d8d8d;
    --card-shadow: rgba(0, 0, 0, 0.12);
  }
  * { box-sizing: border-box; margin: 0; padding: 0; }
  html, body {
    width: 1200px;
    height: 646px;
    overflow: hidden;
    background: var(--backdrop);
  }
  .stage {
    width: 1200px;
    height: 646px;
    display: flex;
    align-items: center;
    justify-content: center;
    gap: 60px;
  }
  .card {
    position: relative;
    width: 500px;
    height: 286px;
    background: var(--card);
    box-shadow: 0 6px 22px var(--card-shadow);
  }

  /* Back of card */
  .card--back .philosophy {
    position: absolute;
    top: 52px;
    left: 0;
    right: 0;
    text-align: center;
    font-family: "Parisienne", cursive;
    font-size: 25px;
    line-height: 1.32;
    color: var(--ink-soft);
  }
  .card--back .contact {
    position: absolute;
    left: 36px;
    right: 36px;
    bottom: 34px;
    display: flex;
    justify-content: space-between;
    font-family: "Inter", sans-serif;
    font-weight: 300;
    font-size: 14px;
    letter-spacing: 0.2px;
    color: var(--ink-soft);
  }

  /* Front of card */
  .card--front .brand {
    position: absolute;
    right: 30px;
    bottom: 44px;
    text-align: right;
    font-family: "Inter", sans-serif;
    font-weight: 300;
    color: var(--ink-logo);
  }
  .card--front .wordmark {
    font-size: 46px;
    line-height: 1;
    letter-spacing: -1.5px;
    text-transform: uppercase;
  }
  .card--front .locations {
    margin-top: 8px;
    font-size: 15px;
    letter-spacing: 1px;
    text-transform: uppercase;
    color: var(--ink-soft);
  }
</style>
</head>
<body>
  <main class="stage">
    <section class="card card--back" aria-label="Back of business card">
      <p class="philosophy">
        Dermavale is the whole body approach to<br>
        beauty. customized medical grade skincare.<br>
        massage. wellness counsel.<br>
        By appointment only!
      </p>
      <div class="contact">
        <span class="website">www.dermavalewellness-example.com</span>
        <span class="phone">p: (555) 318-2406</span>
      </div>
    </section>

    <section class="card card--front" aria-label="Front of business card">
      <div class="brand">
        <div class="wordmark">Dermavale</div>
        <div class="locations">Lakemere | Harbor Bay | Dune Point</div>
      </div>
    </section>
  </main>
</body>
</html>
```